kestrova business cards

Hey design gurus!
I'm after a clean, modern, stylish business card for my about to be launched company.
I've uploaded the logos for my company "Kestrova Electrical Solutions"
and also the tarrow alliance logo to whom i am associated.

```html
<!DOCTYPE html>
<html lang="en">
<head>
<meta charset="utf-8">
<title>Kestrova Electrical Solutions – Business Cards</title>
<link rel="stylesheet" href="https://fonts.googleapis.com/css2?family=Montserrat:wght@700;800;900&family=Poppins:wght@400;500&display=swap">
<style>
  :root {
    --stage: #2b2b2d;
    --navy: #0b1922;
    --blue: #1a7fd0;
    --ink: #111315;
    --paper: #ffffff;
    --muted: #8a97a3;
  }
  * { box-sizing: border-box; margin: 0; padding: 0; }
  html, body { width: 1200px; height: 880px; overflow: hidden; }
  body {
    background: var(--stage);
    display: flex; align-items: center; justify-content: center; gap: 30px;
    font-family: "Poppins", sans-serif;
  }
  .card {
    position: relative; width: 560px; height: 320px; overflow: hidden;
    box-shadow: 0 18px 40px rgba(0,0,0,.45);
  }
  .card--back { background: var(--navy); }
  .card--front { background: var(--paper); }

  .brand { position: absolute; display: flex; align-items: center; gap: 12px; }
  .brand__mark {
    width: 46px; height: 46px; border-radius: 50%;
    background: var(--paper); border: 4px solid var(--blue);
  }
  .brand__name {
    font-family: "Montserrat", sans-serif; font-weight: 900;
    color: var(--blue); letter-spacing: .5px; line-height: 1;
  }
  .brand__tag {
    font-family: "Montserrat", sans-serif; font-weight: 800;
    letter-spacing: 2.6px; line-height: 1; margin-top: 4px;
  }
  .card--back .brand { left: 150px; top: 132px; }
  .card--back .brand__name { font-size: 44px; }
  .card--back .brand__tag { color: var(--paper); font-size: 11.5px; }

  .partner-badge {
    position: absolute; right: 26px; bottom: 26px;
    width: 132px; height: 36px; border: 1.5px solid #c9d2da; border-radius: 4px;
    display: flex; align-items: center; padding-left: 8px;
  }
  .partner-badge span { width: 22px; height: 22px; background: #e8edf1; border-radius: 2px; }

  .card--front .brand { left: 26px; top: 82px; flex-direction: column; align-items: flex-start; gap: 0; }
  .card--front .brand__name { font-size: 46px; }
  .card--front .brand__tag { color: var(--ink); font-size: 12px; }
  .front-mark {
    position: absolute; right: 40px; top: 18px; width: 136px; height: 136px;
    border-radius: 50%; border: 7px solid var(--blue); background: var(--paper);
  }
  .front-shapes { position: absolute; inset: 0; }

  .holder { position: absolute; left: 26px; top: 186px; color: var(--paper); }
  .holder__name {
    font-family: "Montserrat", sans-serif; font-weight: 900; font-size: 22px;
    color: var(--blue); line-height: 1;
  }
  .holder__role {
    font-family: "Montserrat", sans-serif; font-weight: 800; font-size: 12.5px;
    letter-spacing: 1px; margin-top: 3px;
  }
  .contact { position: absolute; left: 26px; top: 240px; list-style: none; }
  .contact li {
    display: flex; align-items: center; gap: 8px;
    font-size: 13.5px; color: var(--ink); line-height: 1.5;
  }
  .contact svg { width: 11px; height: 11px; fill: var(--blue); flex: none; }
  .address {
    position: absolute; right: 26px; top: 192px; text-align: right;
    font-size: 12.5px; color: var(--ink); line-height: 1.35;
  }
</style>
</head>
<body>

<section class="card card--back" aria-label="Card back">
  <div class="brand">
    <span class="brand__mark"></span>
    <div>
      <div class="brand__name">KESTROVA</div>
      <div class="brand__tag">ELECTRICAL SOLUTIONS</div>
    </div>
  </div>
  <div class="partner-badge" aria-label="Tarrow Alliance partner badge"><span></span></div>
</section>

<section class="card card--front" aria-label="Card front">
  <svg class="front-shapes" viewBox="0 0 560 320" aria-hidden="true">
    <polygon points="0,176 300,176 318,164 560,164 560,171 322,171 300,232 0,232" fill="var(--ink)"/>
    <polygon points="360,268 374,246 560,246 560,268" fill="var(--blue)"/>
    <rect x="360" y="268" width="200" height="52" fill="var(--paper)"/>
  </svg>
  <div class="front-mark"></div>
  <div class="brand">
    <div class="brand__name">KESTROVA</div>
    <div class="brand__tag">ELECTRICAL SOLUTIONS</div>
  </div>
  <div class="holder">
    <div class="holder__name">ALDOUS FENWICK</div>
    <div class="holder__role">MANAGING DIRECTOR</div>
  </div>
  <ul class="contact">
    <li><svg viewBox="0 0 24 24"><path d="M6.6 10.8a15.1 15.1 0 006.6 6.6l2.2-2.2c.3-.3.7-.4 1-.2 1.1.4 2.3.6 3.6.6.6 0 1 .4 1 1V20c0 .6-.4 1-1 1A17 17 0 013 4c0-.6.4-1 1-1h3.5c.6 0 1 .4 1 1 0 1.3.2 2.5.6 3.6.1.3 0 .7-.2 1z"/></svg>555-318-0742</li>
    <li><svg viewBox="0 0 24 24"><path d="M2 5h20v14H2z M2 5l10 8 10-8"/></svg>aldous@kestrova-mail.com</li>
    <li><svg viewBox="0 0 24 24"><circle cx="12" cy="12" r="10"/></svg>www.kestrova-electric.com</li>
  </ul>
  <address class="address" style="font-style:normal">
    418 Larchmont Street<br>Suite 12, Brennick<br>OH 43021
  </address>
</section>

</body>
</html>
```